postcard design for moving company

Bramwell  Movers and Storage -moving company , we send postcards to potential clients that have their houses for sale. Must be a postard that is easy to read , where you can notice some deals, reason not to throw the card to junk.
family owned and operated company.
Free estimate
Flat Rate , license and insured, then we must put the zindle and vork 5 stars.
coupons:
$50 Off for all long distance moving
1 month Free Storage for out of state moves.
5% Off for seniors nd veterans.

```html
<!DOCTYPE html>
<html lang="en">
<head>
<meta charset="utf-8">
<title>Bramwell Movers and Storage – Postcard</title>
<link href="https://fonts.googleapis.com/css2?family=Fira+Sans:wght@300;400;500;600;700&family=Oswald:wght@500;600&display=swap" rel="stylesheet">
<style>
  :root{
    --red:#e04e4e;
    --red-deep:#d84545;
    --dark:#2b2b2b;
    --cream:#efece6;
    --white:#ffffff;
    --ink:#2a2a2a;
    --stage:#d2d2d2;
    --line:#9a9a9a;
  }
  *{margin:0;padding:0;box-sizing:border-box}
  html,body{width:1200px;height:904px;overflow:hidden;background:var(--stage)}
  body{position:relative;font-family:"Fira Sans",Arial,sans-serif}
  .card{position:absolute;width:509px;height:364px;overflow:hidden;box-shadow:0 3px 10px rgba(0,0,0,.18)}
  .card--front{left:188px;top:75px;background:var(--cream)}
  .card--back{left:503px;top:465px;background:var(--white)}
  .abs{position:absolute}
  .shapes{position:absolute;left:0;top:0}
  .photo{position:absolute}
  .brand{font-weight:500;color:var(--red);line-height:1.02;letter-spacing:-.2px}

  /* front */
  .front-photo{left:215px;top:0;width:294px;height:290px;background:linear-gradient(135deg,#c9c8cf 0%,#e8dcd3 45%,#f3ede8 70%,#cfcfd6 100%)}
  .inset-photo{border-radius:50%;border:3px solid var(--cream);background:radial-gradient(circle at 55% 45%,#4a5566 0%,#8b8a87 45%,#c8b79e 100%)}
  .front-inset{left:245px;top:146px;width:146px;height:146px}
  .front-brand{left:23px;top:18px;font-size:21px}
  .headline{left:22px;top:104px;color:var(--white);font-weight:700;font-size:14.2px;line-height:17px;text-transform:uppercase}
  .perks{left:22px;top:159px;list-style:none;color:var(--white);font-size:9.6px;line-height:14px;width:230px}
  .perks li{position:relative;padding-left:11px}
  .perks li::before{content:"";position:absolute;left:0;top:4px;width:6px;height:6px;border-radius:50%;background:var(--white)}
  .coupon{position:absolute;left:21px;width:200px;height:32px;border:1.5px solid var(--white);border-radius:3px;display:flex;overflow:hidden}
  .coupon__deal{width:90px;background:var(--cream);color:var(--red);font-family:"Oswald",sans-serif;font-weight:600;display:flex;flex-direction:column;align-items:center;justify-content:center;line-height:1}
  .coupon__deal--big{font-size:25px}
  .coupon__deal sup{font-size:11px;vertical-align:top;margin-right:3px}
  .coupon__deal--stack .main{font-size:17px}
  .coupon__deal--stack .sub{font-size:10px;margin-top:1px}
  .coupon__terms{flex:1;background:var(--red);color:var(--white);font-weight:600;font-size:10.2px;line-height:12.5px;text-transform:uppercase;padding:2px 0 0 8px;display:flex;align-items:center}
  .contact{left:307px;top:300px;list-style:none;color:var(--white);font-weight:300;font-size:12px;line-height:16.5px}
  .contact li{display:flex;align-items:center;gap:6px}
  .dot-icon{width:10px;height:10px;flex:none}

  /* back */
  .back-brand{left:269px;top:19px;font-size:18px}
  .return-address{left:293px;top:55px;font-size:8.6px;line-height:11.5px;color:var(--ink)}
  .stamp{left:426px;top:22px;width:61px;height:61px;border:1px solid #8c8c8c}
  .address-line{position:absolute;left:323px;width:164px;height:0;border-top:1px solid var(--line)}
  .section-title{font-weight:700;font-size:11.6px;text-transform:uppercase}
  .services-title{left:22px;top:20px;color:var(--white)}
  .about{left:22px;top:36px;color:var(--white);font-weight:300;font-size:8.6px;line-height:11.5px}
  .about span{display:block;white-space:nowrap;text-align:justify;text-align-last:justify}
  .about span.last{text-align-last:left}
  .services{left:22px;top:134px;width:245px;list-style:none;color:var(--white);font-weight:500;display:grid;grid-template-columns:125px 120px;grid-auto-flow:column;grid-template-rows:repeat(4,16.2px)}
  .services li{display:flex;align-items:center;gap:4px;font-size:10.4px}
  .services li:nth-child(n+5){font-size:9.8px}
  .tick{width:7px;height:7px;flex:none}
  .why-title{left:22px;top:228px;color:var(--red);font-size:11.6px}
  .reasons{position:absolute;list-style:none;color:var(--white);font-weight:500;font-size:9.4px}
  .reasons li{display:flex;align-items:center;gap:5px;height:16.1px}
  .reasons--main{left:22px;top:243px}
  .reasons--side{left:133px;top:260px}
  .back-inset{left:205px;top:197px;width:128px;height:128px;border-color:var(--white)}
  .team-photo{left:270px;top:220px;width:239px;height:144px;background:linear-gradient(180deg,#3a3a3c 0%,#26262a 55%,#55565a 100%)}
  .back-contact{left:22px;top:339px;display:flex;gap:10px;font-size:10.4px;color:var(--ink);font-weight:500}
  .back-contact span{display:flex;align-items:center;gap:5px}
</style>
</head>
<body>

<!-- Front of the postcard -->
<section class="card card--front" aria-label="Postcard front">
  <div class="photo front-photo" role="img" aria-label="Photo of a smiling family of three holding packing items"></div>

  <svg class="shapes" width="509" height="364" viewBox="0 0 509 364" aria-hidden="true">
    <path d="M0,114 Q70,64 160,66 Q258,72 300,150 Q338,238 250,364 L0,364 Z" fill="var(--red)" stroke="var(--cream)" stroke-width="3"/>
    <path d="M246,366 Q318,262 511,248 L511,366 Z" fill="var(--dark)" stroke="var(--cream)" stroke-width="3"/>
  </svg>

  <div class="photo inset-photo front-inset" role="img" aria-label="Photo of movers unloading boxes from a truck"></div>

  <div class="abs brand front-brand">Bramwell Movers<br>and Storage</div>

  <h1 class="abs headline">A luxury service that<br>goes beyond the traditional<br>moving experience</h1>

  <ul class="abs perks">
    <li>Guaranteed, all-inclusive price</li>
    <li>No hidden costs or surprises</li>
    <li>Labor, protection &amp; transit included. Learn More.</li>
    <li>Boxes, storage, packing, installations &amp; more services available.</li>
  </ul>

  <div class="coupon" style="top:236px">
    <div class="coupon__deal coupon__deal--big"><span><sup>$</sup>50 OFF</span></div>
    <div class="coupon__terms">For all long<br>distance moving</div>
  </div>
  <div class="coupon" style="top:273px">
    <div class="coupon__deal coupon__deal--stack"><span class="main">1 MONTH</span><span class="sub">FREE STORAGE</span></div>
    <div class="coupon__terms">For out of state<br>moves</div>
  </div>
  <div class="coupon" style="top:310px">
    <div class="coupon__deal coupon__deal--big">5% OFF</div>
    <div class="coupon__terms">For seniors nd<br>veterans</div>
  </div>

  <ul class="abs contact">
    <li><svg class="dot-icon" viewBox="0 0 10 10"><circle cx="5" cy="5" r="5" fill="var(--red)"/><path d="M3.2 2.6l1 1-.5.7a3 3 0 0 0 1.9 1.9l.7-.5 1 1-.6.8C4.8 7.4 2.6 5.2 2.5 3.2z" fill="#fff"/></svg>(212) 555-0147</li>
    <li><svg class="dot-icon" viewBox="0 0 10 10"><circle cx="5" cy="5" r="5" fill="var(--red)"/><rect x="2.5" y="3.3" width="5" height="3.6" fill="none" stroke="#fff" stroke-width=".8"/><path d="M2.5 3.3L5 5.3 7.5 3.3" fill="none" stroke="#fff" stroke-width=".8"/></svg>office@gobramwellmovers.com</li>
    <li><svg class="dot-icon" viewBox="0 0 10 10"><circle cx="5" cy="5" r="5" fill="var(--red)"/><circle cx="5" cy="5" r="2.7" fill="none" stroke="#fff" stroke-width=".7"/><path d="M2.3 5h5.4M5 2.3v5.4" stroke="#fff" stroke-width=".6"/></svg>www.gobramwellmovers.com</li>
  </ul>
</section>

<!-- Back of the postcard -->
<section class="card card--back" aria-label="Postcard back">
  <div class="photo team-photo" role="img" aria-label="Photo of the moving crew standing in front of a truck"></div>

  <svg class="shapes" width="509" height="364" viewBox="0 0 509 364" aria-hidden="true">
    <path d="M262,218 Q400,300 511,250 L511,216 Z" fill="var(--white)"/>
    <path d="M0,0 L196,0 Q292,62 296,196 L296,250 L0,250 Z" fill="var(--red)"/>
    <path d="M0,224 Q100,196 200,218 Q250,232 290,262 L290,334 L0,334 Z" fill="var(--dark)" stroke="var(--white)" stroke-width="3"/>
    <rect x="0" y="332" width="286" height="32" fill="var(--white)"/>
    <path d="M286,364 L286,346 Q282,356 276,364 Z" fill="var(--white)"/>
  </svg>

  <div class="photo inset-photo back-inset" role="img" aria-label="Photo of movers wrapping furniture in protective padding"></div>

  <h2 class="abs section-title services-title">Our Services</h2>
  <p class="abs about">
    <span style="width:191px">Although we have an impressive fleet and</span>
    <span style="width:203px">high-quality equipment, it’s our movers we value</span>
    <span style="width:213px">the most. Ensuring that your belongings are safe</span>
    <span style="width:222px">and sound at the arrival and moreover, handling your</span>
    <span style="width:229px">objects as if they were ours, is our core value. We are well</span>
    <span style="width:236px">aware of the fact that one small misstep can ruin</span>
    <span style="width:241px">something either expensive or of sentimental value,</span>
    <span class="last">therefore we leave no room for mistakes.</span>
  </p>

  <ul class="abs services">
    <li><svg class="tick" viewBox="0 0 8 8"><circle cx="4" cy="4" r="4" fill="#fff"/><path d="M2.2 4.1l1.2 1.2 2.4-2.5" fill="none" stroke="var(--red)" stroke-width="1"/></svg>Local Moving</li>
    <li><svg class="tick" viewBox="0 0 8 8"><circle cx="4" cy="4" r="4" fill="#fff"/><path d="M2.2 4.1l1.2 1.2 2.4-2.5" fill="none" stroke="var(--red)" stroke-width="1"/></svg>Commercial Moving</li>
    <li><svg class="tick" viewBox="0 0 8 8"><circle cx="4" cy="4" r="4" fill="#fff"/><path d="M2.2 4.1l1.2 1.2 2.4-2.5" fill="none" stroke="var(--red)" stroke-width="1"/></svg>Long Distance</li>
    <li><svg class="tick" viewBox="0 0 8 8"><circle cx="4" cy="4" r="4" fill="#fff"/><path d="M2.2 4.1l1.2 1.2 2.4-2.5" fill="none" stroke="var(--red)" stroke-width="1"/></svg>Exclusive Division</li>
    <li><svg class="tick" viewBox="0 0 8 8"><circle cx="4" cy="4" r="4" fill="#fff"/><path d="M2.2 4.1l1.2 1.2 2.4-2.5" fill="none" stroke="var(--red)" stroke-width="1"/></svg>Student Moving</li>
    <li><svg class="tick" viewBox="0 0 8 8"><circle cx="4" cy="4" r="4" fill="#fff"/><path d="M2.2 4.1l1.2 1.2 2.4-2.5" fill="none" stroke="var(--red)" stroke-width="1"/></svg>Fine Art &amp; Antique</li>
    <li><svg class="tick" viewBox="0 0 8 8"><circle cx="4" cy="4" r="4" fill="#fff"/><path d="M2.2 4.1l1.2 1.2 2.4-2.5" fill="none" stroke="var(--red)" stroke-width="1"/></svg>Trade Show Movers</li>
    <li><svg class="tick" viewBox="0 0 8 8"><circle cx="4" cy="4" r="4" fill="#fff"/><path d="M2.2 4.1l1.2 1.2 2.4-2.5" fill="none" stroke="var(--red)" stroke-width="1"/></svg>International Moving</li>
  </ul>

  <h2 class="abs section-title why-title">Why Bramwell Movers?</h2>
  <ul class="reasons reasons--main">
    <li><svg class="tick" viewBox="0 0 8 8"><circle cx="4" cy="4" r="4" fill="var(--red)"/><path d="M2.2 4.1l1.2 1.2 2.4-2.5" fill="none" stroke="#fff" stroke-width="1"/></svg>Family Owned &amp; Operated</li>
    <li><svg class="tick" viewBox="0 0 8 8"><circle cx="4" cy="4" r="4" fill="var(--red)"/><path d="M2.2 4.1l1.2 1.2 2.4-2.5" fill="none" stroke="#fff" stroke-width="1"/></svg>Guaranteed Price</li>
    <li><svg class="tick" viewBox="0 0 8 8"><circle cx="4" cy="4" r="4" fill="var(--red)"/><path d="M2.2 4.1l1.2 1.2 2.4-2.5" fill="none" stroke="#fff" stroke-width="1"/></svg>Stellar Service</li>
    <li><svg class="tick" viewBox="0 0 8 8"><circle cx="4" cy="4" r="4" fill="var(--red)"/><path d="M2.2 4.1l1.2 1.2 2.4-2.5" fill="none" stroke="#fff" stroke-width="1"/></svg>Adaptability</li>
    <li><svg class="tick" viewBox="0 0 8 8"><circle cx="4" cy="4" r="4" fill="var(--red)"/><path d="M2.2 4.1l1.2 1.2 2.4-2.5" fill="none" stroke="#fff" stroke-width="1"/></svg>We Are Not Brokers</li>
  </ul>
  <ul class="reasons reasons--side">
    <li><svg class="tick" viewBox="0 0 8 8"><circle cx="4" cy="4" r="4" fill="var(--red)"/><path d="M2.2 4.1l1.2 1.2 2.4-2.5" fill="none" stroke="#fff" stroke-width="1"/></svg>Safe</li>
    <li><svg class="tick" viewBox="0 0 8 8"><circle cx="4" cy="4" r="4" fill="var(--red)"/><path d="M2.2 4.1l1.2 1.2 2.4-2.5" fill="none" stroke="#fff" stroke-width="1"/></svg>Reliable</li>
    <li><svg class="tick" viewBox="0 0 8 8"><circle cx="4" cy="4" r="4" fill="var(--red)"/><path d="M2.2 4.1l1.2 1.2 2.4-2.5" fill="none" stroke="#fff" stroke-width="1"/></svg>Efficient</li>
    <li><svg class="tick" viewBox="0 0 8 8"><circle cx="4" cy="4" r="4" fill="var(--red)"/><path d="M2.2 4.1l1.2 1.2 2.4-2.5" fill="none" stroke="#fff" stroke-width="1"/></svg>Expertise</li>
  </ul>

  <div class="abs back-contact">
    <span><svg class="dot-icon" viewBox="0 0 10 10"><circle cx="5" cy="5" r="5" fill="var(--red)"/><path d="M3.2 2.6l1 1-.5.7a3 3 0 0 0 1.9 1.9l.7-.5 1 1-.6.8C4.8 7.4 2.6 5.2 2.5 3.2z" fill="#fff"/></svg>(212) 555-0147</span>
    <span><svg class="dot-icon" viewBox="0 0 10 10"><circle cx="5" cy="5" r="5" fill="var(--red)"/><circle cx="5" cy="5" r="2.7" fill="none" stroke="#fff" stroke-width=".7"/><path d="M2.3 5h5.4M5 2.3v5.4" stroke="#fff" stroke-width=".6"/></svg>www.gobramwellmovers.com</span>
  </div>

  <div class="abs brand back-brand">Bramwell Movers<br>and Storage</div>
  <p class="abs return-address">418 Harlow Ave #204, New York,<br>&nbsp;&nbsp;NY 10018, USA</p>
  <div class="abs stamp" aria-label="Stamp area"></div>
  <span class="address-line" style="top:142px"></span>
  <span class="address-line" style="top:166px"></span>
  <span class="address-line" style="top:189px"></span>
</section>

</body>
</html>
```